Web Design Project for Industrial Hemp

I'm launching a new company to grow Industrial Hemp and then to set up a manufacturing facility to process the crop each and every year. We require a complete end to end brand and livery suite and we will start with a web presence. We want to appeal to (a) Investors, Employees, Farmers, and consumers so as to engage with all our stakeholders. We want to create a whole new industry that becomes a game changer for environmentally friendly crop production. Hemp is gaining in popularity and credibility across the world!

Target Market(s)

Farmers to produce, Manufacturers who will purchase the raw materials, Investors who will invest in the project, Consumers who will buy Hemp Products

Industry/Entity Type

Industry

Requirements
Must have
• Environmentally Friendly
Carbon Neutral/Positive
Game Changer
Multi-Use Crop
50,000 products can be made from Hemp
Should not have
• Should avoid its relationship with cannabis but not ignore it! When the regulatory bodies acknowledge the benefits of cannabanoids, they will start to legalise the production of cannabis for sale on prescription

```html
<!DOCTYPE html>
<html lang="en">
<head>
<meta charset="utf-8">
<title>Greenfield Fibre Co</title>
<link rel="stylesheet" href="https://fonts.googleapis.com/css2?family=Open+Sans:wght@300;400;600;700&display=swap">
<style>
:root{
  --page:#eeece2;
  --panel:#f7f6f0;
  --leaf:#b5d68c;
  --leaf-deep:#a3c874;
  --nav:#9b9b98;
  --body-text:#666661;
  --accent:#e3281c;
  --footer:#5e5c54;
  --footer-dark:#4f4d46;
  --footer-text:#d8d6cc;
  --icon:#a9a9a6;
}
*{box-sizing:border-box;margin:0;padding:0}
html,body{width:1200px;height:900px;overflow:hidden}
body{background:var(--page);font-family:"Open Sans",Arial,sans-serif;position:relative}
.panel{position:absolute;left:95px;top:0;width:1010px;height:900px;background:var(--panel)}
.site{position:absolute;left:167px;top:10px;width:866px;height:883px}

.brand{position:absolute;left:0;top:0;width:133px;height:132px;background:var(--leaf);display:flex;align-items:flex-end;padding:0 4px 6px}
.brand-name{color:#fff;font-weight:700;font-size:11px;line-height:14px;white-space:nowrap}

.search{position:absolute;left:585px;top:22px;display:flex;gap:5px}
.search-field{width:161px;height:21px;border:1px solid #e2e0d6;background:#fff;font-size:8px;letter-spacing:.5px;color:#b3b1a8;padding:5px 6px}
.search-send{width:31px;height:21px;border:1px solid #e2e0d6;background:#fff;font-size:8px;color:#b3b1a8;text-align:center;padding-top:5px}

.blog{position:absolute;left:798px;top:0;width:67px;height:66px}
.blog span{position:absolute;left:0;top:24px;width:67px;text-align:center;color:#fff;font-size:11px;font-weight:600;letter-spacing:1px}

.nav{position:absolute;left:155px;top:116px;display:flex;font-size:12px;font-weight:600;letter-spacing:0;color:var(--nav);white-space:nowrap}
.nav a{color:var(--nav);text-decoration:none}
.nav a.current{color:var(--leaf-deep)}
.nav .sep{margin:0 6px;color:#bcbcb8;font-weight:400}
.social{position:absolute;left:745px;top:108px;display:flex;gap:10px}
.social span{width:22px;height:22px;border-radius:50%;background:var(--icon)}

.hero{position:absolute;left:0;top:140px;width:866px;height:308px;background:linear-gradient(100deg,#2f4a2a 0%,#4d6e35 30%,#b86a2a 48%,#5b8a3a 62%,#4b7a30 100%)}
.hero-dots{position:absolute;left:784px;top:427px;display:flex;gap:7px}
.hero-dots span{width:13px;height:13px;border-radius:50%;background:#d9ecc6}
.hero-dots span.active{background:#fff;border:3px solid #a33}
.hero-caption{position:absolute;left:0;top:448px;width:866px;height:75px;background:#a8cc82;color:#fff;font-weight:300;font-size:15px;line-height:20.5px;padding:6px 14px 0 27px}
.more{color:var(--accent);font-weight:600;font-size:12px;text-decoration:none}

.feature{position:absolute;top:544px;width:199px}
.feature-image{height:136px;position:relative}
.feature-title{position:absolute;left:0;bottom:0;width:100%;min-height:34px;background:rgba(60,60,56,.62);color:#fff;font-size:12px;line-height:15px;padding:8px 8px 3px}
.feature-text{font-size:10.2px;line-height:13.6px;color:var(--body-text);padding:6px 6px 0 8px;letter-spacing:-.1px}
.feature-text .more{font-size:10.2px;font-weight:400}
.divider{position:absolute;top:544px;width:1px;height:228px;background:#e3e1d8}

.footer{position:absolute;left:0;top:783px;width:866px;height:90px;background:linear-gradient(#63615a,var(--footer-dark));color:var(--footer-text);font-size:8.5px}
.footer-contact{position:absolute;left:12px;top:12px}
.footer-heading{font-size:9px;letter-spacing:.5px;margin-left:15px;margin-bottom:5px}
.footer-row{display:flex;gap:8px;line-height:15px}
.footer-lines{position:absolute;left:232px;top:28px}
.footer-lines .footer-row{align-items:center}
.badges{position:absolute;left:502px;top:10px;display:flex;gap:7px}
.badges span{width:44px;height:44px;border-radius:50%;border:2px solid #c9c7bd;opacity:.7}
.newsletter{position:absolute;left:662px;top:8px;width:200px;height:74px;border:1px solid #7b7970;padding:4px 5px}
.newsletter-title{font-style:italic;font-size:9px;margin-bottom:3px}
.nl-field{height:17px;background:#8a8880;color:#d0cec4;font-style:italic;font-size:9px;padding:3px 6px;margin-bottom:5px}
.nl-row{display:flex;gap:4px}
.nl-row .nl-field{flex:1}
.nl-button{width:50px;height:17px;background:#8cc063;color:#fff;font-size:9px;text-align:center;padding-top:3px}
</style>
</head>
<body>
<div class="panel"></div>
<div class="site">
  <div class="brand"><span class="brand-name">Greenfield Fibre Co</span></div>

  <div class="search"><div class="search-field">ENTER YOUR SEARCH</div><div class="search-send">SEND</div></div>
  <div class="blog">
    <svg width="67" height="66" viewBox="0 0 67 66"><polygon points="0,0 67,0 67,66 33.5,48 0,66" fill="#b5d68c"/></svg>
    <span>BLOG</span>
  </div>

  <nav class="nav">
    <a class="current" href="#">HOME</a><span class="sep">|</span>
    <a href="#">ABOUT</a><span class="sep">|</span>
    <a href="#">FARMERS</a><span class="sep">|</span>
    <a href="#">MANUFACTURERS</a><span class="sep">|</span>
    <a href="#">INVESTORS</a><span class="sep">|</span>
    <a href="#">CONSUMERS</a><span class="sep">|</span>
    <a href="#">CONTACT</a>
  </nav>
  <div class="social"><span></span><span></span><span></span><span></span></div>

  <div class="hero" role="img" aria-label="Tractor with orange harvesting rig cutting a tall green hemp field"></div>
  <div class="hero-dots"><span></span><span></span><span class="active"></span><span></span></div>
  <p class="hero-caption">A hemp crop needs little to no pesticides and no herbicide control, and it produces oxygen. Under favourable growing conditions expect one tonne of seed, three tonnes of fibre band and six tonnes of hurd (leaf fibre) per hectare. Hemp products are incorporated into eco-construction, cosmetics, fuel, mulch and for livestock bedding. <a class="more" href="#">MORE &gt;</a></p>

  <article class="feature" style="left:0">
    <div class="feature-image" role="img" aria-label="Farmer standing beside harvesting machinery in a field" style="background:linear-gradient(#5f7c8e,#4f7a3c 45%,#3e6a2e)">
      <div class="feature-title">Multi-Use Crop</div>
    </div>
    <p class="feature-text">Hemp grows almost anywhere and requires no pesticides or fertiliser. The plant is good both for the soil and the atmosphere. The potential for Hemp is vast - including sustainable bio-mass (power) and bio-diesel (fuel). <a class="more" href="#">MORE &gt;</a></p>
  </article>
  <div class="divider" style="left:211px"></div>
  <article class="feature" style="left:222px">
    <div class="feature-image" role="img" aria-label="Labelled bundles of coloured hemp yarn" style="background:linear-gradient(135deg,#8a8a86,#c8c5bd 45%,#6e7a5c)">
      <div class="feature-title">Manufacturers who will<br>purchase the raw marterial</div>
    </div>
    <p class="feature-text">Hemp grows almost anywhere and requires no pesticides or fertiliser. The plant is good both for the soil and the atmosphere. The potential for Hemp is vast - including sustainable bio-mass (power) and bio-diesel (fuel). <a class="more" href="#">MORE &gt;</a></p>
  </article>
  <div class="divider" style="left:433px"></div>
  <article class="feature" style="left:445px">
    <div class="feature-image" role="img" aria-label="Businessman holding a business magazine" style="background:linear-gradient(120deg,#2a2a2c,#5a4a40 55%,#3a3634)">
      <div class="feature-title">Game Changer</div>
    </div>
    <p class="feature-text">Hemp grows almost anywhere and requires no pesticides or fertiliser. The plant is good both for the soil and the atmosphere. The potential for Hemp is vast - including sustainable bio-mass (power) and bio-diesel (fuel). <a class="more" href="#">MORE &gt;</a></p>
  </article>
  <div class="divider" style="left:656px"></div>
  <article class="feature" style="left:667px">
    <div class="feature-image" role="img" aria-label="Man presenting bottles of hemp oil products" style="background:linear-gradient(90deg,#3a3a30,#7a6a4a 45%,#c9d64a 75%,#3f6f9a)">
      <div class="feature-title">50,000 products can be<br>made from Hemp</div>
    </div>
    <p class="feature-text">Hemp grows almost anywhere and requires no pesticides or fertiliser. The plant is good both for the soil and the atmosphere. The potential for Hemp is vast - including sustainable bio-mass (power) and bio-diesel (fuel). <a class="more" href="#">MORE &gt;</a></p>
  </article>

  <footer class="footer">
    <div class="footer-contact">
      <div class="footer-heading">CONTACT</div>
      <div class="footer-row">
        <svg width="9" height="13" viewBox="0 0 9 13"><path d="M4.5 0A4.5 4.5 0 0 0 0 4.5C0 8 4.5 13 4.5 13S9 8 9 4.5A4.5 4.5 0 0 0 4.5 0z" fill="#cfcdc3"/><circle cx="4.5" cy="4.5" r="1.7" fill="#5e5c54"/></svg>
        <div>Greenfield Fibre Co Ltd<br>12 Meadow Lane, Riverside Valley,<br>Countyshire.</div>
      </div>
    </div>
    <div class="footer-lines">
      <div class="footer-row"><svg width="10" height="12" viewBox="0 0 10 12"><rect x="2" y="0" width="6" height="12" rx="1" fill="none" stroke="#cfcdc3" stroke-width="1.3"/></svg>Phone: +000 (0)11 2223334</div>
      <div class="footer-row"><svg width="12" height="10" viewBox="0 0 12 10"><rect x="0.5" y="0.5" width="11" height="9" fill="none" stroke="#cfcdc3"/><line x1="0.5" y1="4" x2="11.5" y2="4" stroke="#cfcdc3"/></svg>Fax: +000 (0)11 2223335</div>
      <div class="footer-row"><svg width="12" height="10" viewBox="0 0 12 10"><rect x="0.5" y="0.5" width="11" height="9" fill="none" stroke="#cfcdc3"/><polyline points="0.5,0.5 6,5.5 11.5,0.5" fill="none" stroke="#cfcdc3"/></svg>Email: hello@greenfieldfibre.example</div>
    </div>
    <div class="badges"><span></span><span></span><span></span></div>
    <div class="newsletter">
      <div class="newsletter-title">Get our newsletter</div>
      <div class="nl-field">Enter your name</div>
      <div class="nl-row"><div class="nl-field">Enter your email</div><div class="nl-button">Sign Up</div></div>
    </div>
  </footer>
</div>
</body>
</html>
```